Biography of the Prophet Zeravin

We need a great book cover which honors the Name of the Prophet Zeravin. It should be classic clean and has islamic elements. It is a book in german language. I attached the informations which should be placed on the front- and backcover.

Target Market(s)

Islamic. Germany.

Font styles to use
Serif

Colors

Designer to choose colors to be used in the design.

Requirements
Must have
• Must include all texts i've attached in the pdfs.

```html
<!DOCTYPE html>
<html lang="de">
<head>
<meta charset="utf-8">
<title>Zeravin – Buchcover</title>
<link rel="stylesheet" href="https://fonts.googleapis.com/css2?family=Cinzel:wght@400;500&family=Alegreya:ital,wght@0,400;1,400&display=swap">
<style>
  :root {
    --stage: #c9d3d3;
    --navy: #1c2a52;
    --navy-deep: #121c3a;
    --gold: #d9b45a;
    --gold-light: #f1d88e;
    --gold-dark: #8a6422;
    --text-cream: #e9dcb6;
  }
  * { margin: 0; padding: 0; box-sizing: border-box; }
  html, body {
    width: 1200px;
    height: 1118px;
    overflow: hidden;
    background: var(--stage);
  }
  .cover {
    position: absolute;
    left: 272px;
    top: 39px;
    width: 656px;
    height: 1040px;
    background: radial-gradient(ellipse at 50% 40%, #263769 0%, var(--navy) 55%, var(--navy-deep) 100%);
    overflow: hidden;
  }
  .frame-ornament {
    position: absolute;
    inset: 0;
    border: 44px solid transparent;
    border-image: linear-gradient(135deg, var(--gold-dark), var(--gold-light) 30%, var(--gold) 55%, var(--gold-dark) 80%, var(--gold-light)) 1;
    opacity: 0.85;
  }
  .frame-line {
    position: absolute;
    inset: 50px;
    border: 1px solid var(--gold);
    opacity: 0.6;
  }
  .medallion {
    position: absolute;
    left: 50%;
    top: 158px;
    width: 268px;
    height: 268px;
    transform: translateX(-50%);
    border-radius: 50%;
    background: radial-gradient(circle, rgba(241,216,142,0.55) 0%, rgba(217,180,90,0.35) 45%, rgba(217,180,90,0.12) 75%, rgba(217,180,90,0) 100%);
    border: 1.5px solid var(--gold);
  }
  .title {
    position: absolute;
    top: 470px;
    width: 100%;
    text-align: center;
    font-family: "Cinzel", serif;
    font-weight: 500;
    font-size: 82px;
    letter-spacing: 1px;
    color: var(--gold);
    background: linear-gradient(180deg, var(--gold-light), var(--gold) 55%, var(--gold-dark));
    -webkit-background-clip: text;
    background-clip: text;
    -webkit-text-fill-color: transparent;
  }
  .subtitle {
    position: absolute;
    top: 575px;
    width: 100%;
    text-align: center;
    font-family: "Alegreya", serif;
    font-size: 18px;
    line-height: 29px;
    color: var(--text-cream);
  }
  .divider-ornament {
    position: absolute;
    left: 50%;
    top: 688px;
    width: 14px;
    height: 44px;
    transform: translateX(-50%);
    border-radius: 7px;
    background: linear-gradient(180deg, var(--gold-light), var(--gold-dark));
  }
  .credits {
    position: absolute;
    top: 755px;
    width: 100%;
    text-align: center;
    font-family: "Alegreya", serif;
    font-style: italic;
    font-size: 17.5px;
    line-height: 29px;
    color: var(--text-cream);
  }
  .publisher {
    position: absolute;
    top: 862px;
    width: 100%;
    display: flex;
    flex-direction: column;
    align-items: center;
    gap: 8px;
  }
  .publisher-mark {
    width: 40px;
    height: 40px;
    border: 1.5px solid var(--text-cream);
  }
  .publisher-name {
    font-family: "Alegreya", serif;
    font-size: 12px;
    color: var(--text-cream);
  }
</style>
</head>
<body>
  <main class="cover">
    <div class="frame-ornament" role="img" aria-label="Goldene florale Ornamentbordüre rund um das Cover"></div>
    <div class="frame-line"></div>

    <div class="medallion" role="img" aria-label="Goldenes geometrisches islamisches Sternmedaillon"></div>

    <h1 class="title">ZERAVIN</h1>

    <p class="subtitle">
      Seine Lebensgeschichte,<br>
      Fakten aus seinem Alltag<br>
      und seine Besonderheiten
    </p>

    <div class="divider-ornament" role="img" aria-label="Kleines goldenes Zierornament"></div>

    <p class="credits">
      Von ʾAbū al-Ḥasan Yūsuf ibn Ṭāriq ibn Saʿdān<br>
      Übersetzt und kommentiert von Harun Feldmoser
    </p>

    <div class="publisher">
      <div class="publisher-mark"></div>
      <span class="publisher-name">Haus der Schriften</span>
    </div>
  </main>
</body>
</html>
```